Postcard: Open Sky Circle

Text for front: HOW TO CHANGE THE WORLD IN ONE [note: the word "one" should be underlined] STEPHint: It's up to you...[Note: add arrow or something to indicate "turn over"]Text for back: You're going to spend your entire life with someone you can never get away from. (Guess who?) Wouldn't you rather that person #OpenSkyCircle than judgmental or critical? BE the change you want to see! Visit www.OpenSkyCircle-hub.example for daily Dawn Pebbles and community. PLEASE JOIN US![Note: add logo to left half of back side]Font preference for text: Josefin sans

Target Market(s)

People who would be attracted to Corvane church - teravian perennist message. It's spiritual without being overtly religious, so the target market is probably early 30s and up but ideally won't turn off Millennials (folks under 30). It should attract attention of people who are open-minded and committed to progressive social change, tired of an atmosphere of hate-mongering and divisiveness.

Requirements
Nice to have
• It would be nice to convey a sense of challenge - there is an idea of "dawn pebbles" so something related to fire/sparks is appropriate. This is meant to evoke a deeper, divine love more than a sense of romantic love. This love is more fierce than fluffy! Yet it calls us to be our best selves.
Should not have
• Please avoid excessive pink - just the logo is enough, as this design needs to appeal to men as well as women.

```html
<!DOCTYPE html>
<html lang="en">
<head>
<meta charset="utf-8">
<title>Open Sky Circle Postcard</title>
<link rel="stylesheet" href="https://fonts.googleapis.com/css2?family=Arimo:ital,wght@0,400;0,700;1,400;1,700&family=Cinzel+Decorative:wght@400;700;900&display=swap">
<style>
  :root {
    --backdrop: #4a4a4a;
    --paper: #ffffff;
    --wash: #ee4f55;
    --wash-soft: rgba(238, 79, 85, 0.55);
    --glow: rgba(242, 140, 60, 0.10);
    --flame: #d9381a;
    --flame-deep: #9c1c10;
    --ember: #f2a33a;
    --ink: #111111;
    --join-red: #e0171f;
  }
  * { margin: 0; padding: 0; box-sizing: border-box; }
  html, body {
    width: 1200px; height: 1200px; overflow: hidden;
    background: var(--backdrop);
  }
  .postcard {
    position: absolute; left: 260px; width: 682px;
    background: var(--paper); overflow: hidden;
  }
  .postcard--front { top: 38px; height: 530px; }
  .postcard--back { top: 609px; height: 527px; }

  .wash { position: absolute; border-radius: 50%; }
  .wash--front-top {
    left: -60px; top: -80px; width: 520px; height: 190px;
    background: radial-gradient(ellipse at 40% 45%, var(--wash) 0%, var(--wash-soft) 45%, rgba(238,79,85,0) 72%);
  }
  .wash--front-right {
    left: 500px; top: 240px; width: 320px; height: 360px;
    background: radial-gradient(ellipse at 60% 55%, var(--wash) 0%, var(--wash) 35%, var(--wash-soft) 55%, rgba(238,79,85,0) 72%);
  }
  .wash--front-bottom {
    left: 80px; top: 470px; width: 480px; height: 110px;
    background: radial-gradient(ellipse at 60% 70%, var(--wash-soft) 0%, rgba(238,79,85,0) 70%);
  }
  .wash--back-top {
    left: 360px; top: -90px; width: 420px; height: 230px;
    background: radial-gradient(ellipse at 55% 45%, var(--wash) 0%, var(--wash-soft) 45%, rgba(238,79,85,0) 72%);
  }
  .wash--back-right {
    left: 600px; top: 60px; width: 160px; height: 440px;
    background: radial-gradient(ellipse at 70% 50%, var(--wash-soft) 0%, rgba(238,79,85,0) 70%);
  }
  .wash--back-bottom-left {
    left: -120px; top: 360px; width: 380px; height: 260px;
    background: radial-gradient(ellipse at 35% 60%, var(--wash) 0%, var(--wash-soft) 45%, rgba(238,79,85,0) 72%);
  }
  .wash--back-bottom-right {
    left: 390px; top: 460px; width: 260px; height: 120px;
    background: radial-gradient(ellipse at 50% 70%, var(--wash-soft) 0%, rgba(238,79,85,0) 70%);
  }

  .title-glow {
    position: absolute; left: 66px; top: 40px; width: 520px; height: 430px;
    border-radius: 50%;
    background: radial-gradient(ellipse at 50% 50%, var(--glow) 0%, rgba(242,140,60,0) 70%);
  }

  .headline {
    position: absolute; left: 64px; top: 112px; width: 520px;
    font-family: "Cinzel Decorative", serif; font-weight: 900;
    font-size: 52px; line-height: 60px; text-align: center;
    color: var(--flame);
    text-shadow: 1px 1px 0 var(--flame-deep), 0 0 2px var(--ember);
    letter-spacing: -1px;
  }
  .headline__underline { text-decoration: underline; text-decoration-thickness: 2px; text-underline-offset: 4px; }

  .hint {
    position: absolute; left: 60px; top: 452px;
    font-family: "Arimo", sans-serif; font-style: italic;
    font-size: 23px; color: var(--ink); letter-spacing: 0.5px;
  }
  .hint strong { font-weight: 700; }

  .turn-arrow { position: absolute; left: 0; top: 0; }

  .logo-panel {
    position: absolute; left: 16px; top: 39px; width: 350px; height: 352px;
    background: var(--paper);
  }
  .brand-mark {
    position: absolute; left: 40px; top: 180px; width: 270px;
    display: flex; align-items: center; justify-content: center; gap: 10px;
    font-family: "Arimo", sans-serif; font-weight: 700; font-size: 24px;
    color: var(--join-red);
  }
  .brand-mark__dot {
    width: 18px; height: 18px; border-radius: 50%; background: var(--join-red);
  }

  .message {
    position: absolute; left: 361px; top: 102px; width: 240px;
    font-family: "Arimo", sans-serif; font-size: 13.3px; line-height: 19.5px;
    color: var(--ink);
  }
  .message p { margin-bottom: 10px; }
  .message .visit { margin-bottom: 0; white-space: nowrap; }
  .message .visit strong { font-size: 14.5px; }

  .join-rule {
    position: absolute; left: 107px; width: 467px; height: 1px;
    background: var(--join-red);
  }
  .join-rule--top { top: 374px; }
  .join-rule--bottom { top: 455px; }
  .join-call {
    position: absolute; left: 60px; top: 384px; width: 562px;
    text-align: center;
    font-family: "Cinzel Decorative", serif; font-weight: 400;
    font-size: 46px; line-height: 60px; color: var(--join-red);
  }
</style>
</head>
<body>

<section class="postcard postcard--front" aria-label="Postcard front">
  <div class="wash wash--front-top" role="img" aria-label="Red watercolour wash"></div>
  <div class="wash wash--front-right" role="img" aria-label="Red watercolour wash"></div>
  <div class="wash wash--front-bottom" role="img" aria-label="Red watercolour wash"></div>

  <div class="title-glow" role="img" aria-label="Decorative fiery heart outline around the title"></div>

  <h1 class="headline">HOW TO<br>CHANGE THE<br>WORLD<br>IN <span class="headline__underline">ONE</span> STEP</h1>

  <svg class="turn-arrow" width="682" height="530" viewBox="0 0 682 530" aria-hidden="true">
    <path d="M 478 338 L 478 416 L 600 416" fill="none" stroke="var(--ember)" stroke-width="3"/>
    <path d="M 486 338 L 486 408 L 600 408" fill="none" stroke="var(--flame)" stroke-width="3"/>
    <path d="M 580 392 L 618 410 L 580 428" fill="none" stroke="var(--flame-deep)" stroke-width="3"/>
  </svg>

  <p class="hint">Hint: <strong>It's up to you...</strong></p>
</section>

<section class="postcard postcard--back" aria-label="Postcard back">
  <div class="wash wash--back-top" role="img" aria-label="Red watercolour wash"></div>
  <div class="wash wash--back-right" role="img" aria-label="Red watercolour wash"></div>
  <div class="wash wash--back-bottom-left" role="img" aria-label="Red watercolour wash"></div>
  <div class="wash wash--back-bottom-right" role="img" aria-label="Red watercolour wash"></div>

  <div class="logo-panel">
    <div class="brand-mark"><span class="brand-mark__dot"></span>Open Sky Circle</div>
  </div>

  <div class="message">
    <p>You're going to spend your entire life with someone you can never getaway from.</p>
    <p><strong>(Guess who?)</strong></p>
    <p>Wouldn't you rather that person #OpenSkyCircle than judgmental or critical?</p>
    <p><em>BE the change you want to see!</em></p>
    <p class="visit"><strong>Visit: www.OpenSkyCircle-hub.example</strong><br>for daily Dawn Pebbles and community.</p>
  </div>

  <div class="join-rule join-rule--top"></div>
  <p class="join-call">PLEASE JOIN US!</p>
  <div class="join-rule join-rule--bottom"></div>
</section>

</body>
</html>
```